Vel Oska Concrete Post Card Design Project

Hello, We are A Concrete Contractor. We specialize in removing and replacing concrete walkways, Patio's, Driveway's, ect., that are a trip hazard. We work a lot in Apartment complexes and Business Complexes where the trees have grown big and the roots from the trees lift up the concrete.
I would like someone to design a postcard (Two Sided) so I can send it out and market potential property manager customers. I would like to use our company logo on this card. Please see the pixel vault link below. Here are some things I would like the card to have on it.

1.Removal and Replacement of Concrete Sidewalks, Driveways, Parking Lots, Curb and Gutter.

2. ADA Compliant.

3. Repair of concrete tripping hazards and
root-damaged sidewalks.

4. Vel Oska Concrete brings your sidewalks in compliance with the Americans With Disabilities Act (ADA).

5. Property Management:

We cater to the needs of Property Mangement Companies, HOA, Apartment Complexes, Business Parks, Senior Living Complexes, Government Buildings and Shopping Centers.

6. Free Estimates
7. Contractors license number under our logo. It is:
BPLN #718390
8. Our phone numbers:555-284-9163 and 555-672-0394.

Card should be two sided 9" by 6"

Thank You
Updates

This website would not let me upload my logo so please click on the link below to get it.

 

http://i4471.pixelvault-host.com/albums/k218/Tvoska42/VelOskaConcreteLogo-2012-PROOF-2.jpg

Thank You

Reason: Hello, I have a lot of great designs. I have had a busy week and I am just now sitting down to ask for the changes I would like. Once I recieve all of the designs back with the changes I requested I would like to get the opinions of my coworkers and friends before selecting the design. I am asking for the deadline to be extended by 4 days. Thank You so much, Brenda Vel Oska

Target Market(s)

Property Managers

Industry/Entity Type

Concrete

Requirements
Must have
• Our logo

```html
<!DOCTYPE html>
<html lang="en">
<head>
<meta charset="utf-8">
<title>Vel Oska Concrete – Postcard Back</title>
<link rel="stylesheet" href="https://fonts.googleapis.com/css2?family=Anton&family=Crimson+Pro:wght@700&family=Patrick+Hand&display=swap">
<style>
  :root {
    --page-bg: #ececec;
    --concrete-light: #dedede;
    --concrete-mid: #cbcbcb;
    --brand-red: #e8141b;
    --brand-red-deep: #b5161c;
    --maroon: #8a1e2c;
    --ink: #141414;
    --white: #ffffff;
    --lawn: #5f8f34;
    --walk: #d3d6d4;
    --rebar: #b9644a;
  }
  * { margin: 0; padding: 0; box-sizing: border-box; }
  html, body { width: 1200px; height: 900px; overflow: hidden; }
  body { background: var(--page-bg); position: relative; }

  .postcard {
    position: absolute; left: 0; top: 50px;
    width: 1200px; height: 800px; overflow: hidden;
    font-family: "Crimson Pro", Georgia, serif;
  }
  .concrete-backdrop {
    position: absolute; inset: 0;
    background: radial-gradient(ellipse at 40% 30%, var(--concrete-light), var(--concrete-mid));
  }

  .photo { position: absolute; top: 520px; height: 280px; }
  .photo--walkway-left { left: 0; width: 373px;
    background: linear-gradient(100deg, var(--lawn) 0%, var(--lawn) 38%, var(--walk) 50%, #bfc3c1 70%, #6e9a42 100%); }
  .photo--pour { left: 373px; width: 527px;
    background: linear-gradient(90deg, #b4b1aa 0%, #a29f97 55%, var(--rebar) 75%, #8a6a55 100%); }
  .photo--walkway-right { left: 900px; width: 300px;
    background: linear-gradient(90deg, #5d8a33 0%, var(--walk) 30%, #e3e5e4 60%, #7ea24e 100%); }

  .waves { position: absolute; inset: 0; width: 1200px; height: 800px; }

  .call-badge { position: absolute; left: 49px; top: 28px; width: 240px; height: 240px; }
  .call-badge text { font-family: "Anton", Impact, sans-serif; fill: var(--white); }

  .phone-block {
    position: absolute; left: 24px; top: 290px; width: 300px;
    text-align: center; font-family: "Patrick Hand", "Comic Sans MS", cursive;
    font-size: 40px; line-height: 57px; color: var(--white); letter-spacing: 1px;
    text-shadow: -2px -2px 0 var(--ink), 2px -2px 0 var(--ink), -2px 2px 0 var(--ink), 2px 2px 0 var(--ink),
                 0 2px 0 var(--ink), 0 -2px 0 var(--ink), 2px 0 0 var(--ink), -2px 0 0 var(--ink);
  }

  .selling-points { position: absolute; left: 386px; top: 162px; width: 760px; list-style: none; }
  .selling-points li {
    position: relative; font-size: 24px; line-height: 38px; color: var(--ink);
    text-shadow: 0 0 2px rgba(255,255,255,.8); margin-bottom: 10px;
  }
  .selling-points li::before {
    content: ""; position: absolute; left: -26px; top: 14px; width: 13px; height: 13px;
    border-radius: 50%; background: var(--brand-red); box-shadow: 0 0 0 1.5px var(--maroon);
  }

  .services-title {
    position: absolute; left: 385px; top: 314px; width: 600px; text-align: center;
    font-size: 31px; color: var(--brand-red-deep);
    text-shadow: 0 0 2px rgba(255,255,255,.9);
  }
  .services-list {
    position: absolute; left: 423px; top: 378px; width: 600px; list-style: none;
    display: grid; grid-template-columns: 288px 300px; row-gap: 4px;
  }
  .services-list li { font-size: 24px; line-height: 40px; color: var(--ink); text-shadow: 0 0 2px rgba(255,255,255,.8); }

  .company-sign { position: absolute; left: 1000px; top: 676px; width: 190px; text-align: center; }
  .company-name { font-size: 27px; line-height: 28px; color: var(--brand-red-deep); }
  .company-licence { margin-top: 6px; font-size: 15px; color: var(--ink); letter-spacing: .5px; }
</style>
</head>
<body>
  <main class="postcard">
    <div class="concrete-backdrop" role="img" aria-label="Smooth poured concrete wall surface"></div>

    <div class="photo photo--walkway-left" role="img" aria-label="Curving concrete sidewalk beside a green lawn and street"></div>
    <div class="photo photo--pour" role="img" aria-label="Worker spreading fresh concrete over steel rebar grid"></div>
    <div class="photo photo--walkway-right" role="img" aria-label="Straight new concrete sidewalk between grass strips"></div>

    <svg class="waves" viewBox="0 0 1200 800" preserveAspectRatio="none" aria-hidden="true">
      <!-- top ribbon -->
      <path d="M280 125 C520 140 760 110 1200 95 L1200 190 C900 120 650 140 280 125 Z" fill="var(--brand-red)" opacity=".8"/>
      <path d="M280 128 C520 150 800 40 1200 110" fill="none" stroke="var(--maroon)" stroke-width="4"/>
      <!-- bottom band -->
      <path d="M0 443 C150 480 260 545 430 545 C700 545 950 470 1200 474 L1200 503 C950 500 700 560 460 560 C260 560 120 540 0 518 Z" fill="var(--brand-red)"/>
      <path d="M0 540 C140 580 260 610 420 600 C600 585 700 520 850 530 C1000 540 1100 560 1200 548" fill="none" stroke="var(--maroon)" stroke-width="5"/>
    </svg>

    <svg class="call-badge" viewBox="-120 -120 240 240" role="img" aria-label="Call us now">
      <polygon fill="var(--brand-red)" points="100,0 84.4,16.8 92.4,38.3 71.5,47.8 70.7,70.7 47.8,71.5 38.3,92.4 16.8,84.4 0,100 -16.8,84.4 -38.3,92.4 -47.8,71.5 -70.7,70.7 -71.5,47.8 -92.4,38.3 -84.4,16.8 -100,0 -84.4,-16.8 -92.4,-38.3 -71.5,-47.8 -70.7,-70.7 -47.8,-71.5 -38.3,-92.4 -16.8,-84.4 0,-100 16.8,-84.4 38.3,-92.4 47.8,-71.5 70.7,-70.7 71.5,-47.8 92.4,-38.3 84.4,-16.8" transform="scale(1.15) rotate(-8)"/>
      <circle r="84" fill="var(--white)"/>
      <circle r="79" fill="var(--brand-red)"/>
      <path d="M-79 8 A79 79 0 0 0 79 -20 L79 0 A79 79 0 0 1 -79 0 Z" fill="var(--brand-red-deep)"/>
      <g transform="rotate(-20)">
        <text x="0" y="-12" text-anchor="middle" font-size="38">CALL US</text>
        <text x="0" y="48" text-anchor="middle" font-size="62">NOW</text>
      </g>
    </svg>

    <div class="phone-block">
      <p>555-284-9163</p>
      <p>&amp;</p>
      <p>555-672-0394</p>
    </div>

    <ul class="selling-points">
      <li>Vel Oska Concrete brings your sidewalks in compliance with the Americans With Disabilities Act (ADA).</li>
      <li>Repair of tripping hazard removal, root-damaged sidewalks.</li>
    </ul>

    <h2 class="services-title">Removal &amp; Replacement:</h2>
    <ul class="services-list">
      <li>- Concrete Sidewalks</li>
      <li>- Parking Lots</li>
      <li>- Driveways</li>
      <li>- Curb and Gutters</li>
    </ul>

    <div class="company-sign">
      <p class="company-name">Vel Oska Concrete</p>
      <p class="company-licence">BPLN #718390</p>
    </div>
  </main>
</body>
</html>
```